Postcard to Sell Ads to business

I am in need of a very professional, clean but SEXY postcard that creates excitement to the business owner and gets them to call me to learn more. I expect source file (psd) with final files.

Postcard Requirements

FULL COLOR - FRONT And Back
All Text Editable including heading font uses
Use of Vibrant colors and vector ICONS
Backside should contain text and images as well

Items to Include in design

Benefits of Advertising
- 365 Days of Advertising
- Under $.04 per home
- Unlimited Social Media Attention
- Increased Revenue
- 100% Managed for you

Did You Know Facts
87% of online users depend on the internet to access local discounts
Business who use the internet to promote and sell thier offline goods and services have grown 46% faster over the past two years.

This postcard will sell my Direct Mailer I offer to go along with my local business directoy - http://www.ourvillagesavers.example

Visually connecting this service to a local nature is imperitive.

Target Market(s)

Local area business, Retail, Restaurant, Media, and anything sold to consumers.

Industry/Entity Type

Advertising

Font styles to use
Sans Serif

Requirements
Must have
• Return Address as:
• Our Village Savers
• P.O Box 748
• Putnam, CT 06917
• 1-860-555-0182
• COLOR
• Text based "Logo": Our Village Savers
• Include a emphasis on just $.04/home
• Icons/infographic use
Nice to have
• Vector based character image
• Your Ad Here Image as a representation to what this postcard is about
Should not have
• Large amount of whitespace

```html
<!DOCTYPE html>
<html lang="en">
<head>
<meta charset="utf-8">
<title>Our Village Savers – Advertising Postcard</title>
<link rel="stylesheet" href="https://fonts.googleapis.com/css2?family=Roboto:wght@400;500;700;900&family=Open+Sans:wght@400;600;700&display=swap">
<style>
  :root{
    --blue:#1c45a8;
    --blue-dark:#12307c;
    --yellow:#f7c21b;
    --ink:#1d2433;
    --white:#ffffff;
    --stage:#e9ebef;
    --grey:#b9bcc3;
    --photo-a:#d9c3a2;
    --photo-b:#8c7656;
  }
  *{box-sizing:border-box;margin:0;padding:0}
  html,body{width:849px;height:1200px;overflow:hidden}
  body{background:var(--stage);font-family:"Open Sans",sans-serif;color:var(--ink);position:relative}
  .card{position:absolute;left:30px;width:789px;height:540px;background:var(--white);overflow:hidden;box-shadow:0 6px 18px rgba(0,0,0,.18)}
  .card--front{top:30px}
  .card--back{top:630px}
  .abs{position:absolute}

  /* front */
  .top-band{left:0;top:0;width:789px;height:84px;background:linear-gradient(90deg,var(--blue-dark),var(--blue))}
  .brand{display:flex;align-items:center;gap:12px}
  .brand__dot{width:30px;height:30px;border-radius:50%;background:var(--yellow);flex:none}
  .brand__name{font-family:"Roboto",sans-serif;font-weight:900;color:var(--white);font-size:30px;line-height:1}
  .brand__tag{font-family:"Open Sans",sans-serif;color:var(--yellow);font-size:13px;font-weight:600;margin-top:4px}
  .front-brand{left:26px;top:16px}
  .photo{left:0;top:0}
  .ad-sign{left:580px;top:176px;width:170px;height:80px;background:var(--white);border:3px solid var(--ink);display:flex;flex-direction:column;justify-content:center;align-items:center;font-family:"Roboto",sans-serif;font-weight:900;color:var(--ink);line-height:1.05;transform:rotate(-2deg)}
  .ad-sign span{font-size:22px}
  .headline{left:40px;top:118px;font-family:"Roboto",sans-serif;font-weight:900;line-height:1.08;text-align:center;width:370px}
  .headline .h-blue{color:var(--blue);font-size:44px;display:block}
  .headline .h-ink{color:var(--ink);font-size:44px;display:block}
  .headline .h-small{color:var(--ink);font-size:34px;display:block}
  .call{left:40px;top:340px;width:370px;text-align:center;font-family:"Roboto",sans-serif;font-weight:900;color:var(--blue);line-height:1.1}
  .call__label{font-size:30px}
  .call__number{font-size:30px;color:var(--ink)}
  .divider{left:425px;top:335px;width:3px;height:110px;background:var(--yellow)}
  .features{left:450px;top:340px;list-style:none;font-family:"Roboto",sans-serif;font-weight:700;font-size:17px;color:var(--ink);line-height:1.6}
  .features li{display:flex;align-items:center;gap:10px}
  .features li::before{content:"";width:9px;height:9px;background:var(--blue);flex:none}
  .bottom-band{left:0;top:450px}
  .url{left:0;top:490px;width:789px;text-align:center;font-family:"Roboto",sans-serif;font-weight:700;font-size:22px;letter-spacing:3px;color:var(--white)}

  /* back */
  .intro{left:24px;top:20px;width:370px;font-size:11.5px;line-height:1.5;color:var(--ink)}
  .back-panel{left:0;top:0}
  .benefits{left:34px;top:178px;color:var(--white)}
  .benefits__title{font-family:"Roboto",sans-serif;font-weight:900;font-size:26px;color:var(--yellow);margin-bottom:6px}
  .benefits__list{list-style:none;font-family:"Roboto",sans-serif;font-weight:500;font-size:15px;line-height:1.55}
  .benefits__list li{display:flex;align-items:center;gap:8px}
  .benefits__list li::before{content:"";width:7px;height:7px;border-radius:50%;background:var(--yellow);flex:none}
  .fact{left:34px;top:340px;width:360px;font-size:12px;line-height:1.45;color:var(--white)}
  .back-brand{left:34px;top:430px}
  .back-brand .brand__name{font-size:24px}
  .back-brand .brand__dot{width:24px;height:24px}
  .back-brand .brand__tag{font-size:11px}
  .return{left:70px;top:478px;font-family:"Roboto",sans-serif;font-weight:700;font-size:13px;color:var(--white);line-height:1.35}
  .stamp{left:680px;top:26px;width:80px;height:80px;background:var(--grey)}
  .price{left:438px;top:100px;width:170px;height:170px;border-radius:50%;background:var(--blue);border:8px solid var(--yellow);display:flex;flex-direction:column;align-items:center;justify-content:center;color:var(--white);font-family:"Roboto",sans-serif}
  .price__value{font-size:50px;font-weight:900;line-height:1}
  .price__unit{font-size:24px;font-weight:700}
  .growth{left:596px;top:250px;width:104px;height:104px;border-radius:50%;background:var(--yellow);border:5px solid var(--white);box-shadow:0 0 0 3px var(--blue);display:flex;flex-direction:column;align-items:center;justify-content:center;color:var(--blue);font-family:"Roboto",sans-serif;font-weight:900;line-height:1}
  .growth__value{font-size:34px}
  .growth__unit{font-size:22px}
  .mail-lines{left:540px;top:400px;width:220px}
  .mail-lines span{display:block;height:1px;background:var(--grey);margin-bottom:28px}
</style>
</head>
<body>

<section class="card card--front" aria-label="Postcard front">
  <svg class="abs photo" width="789" height="540" viewBox="0 0 789 540" aria-hidden="true">
    <defs>
      <linearGradient id="photoTone" x1="0" y1="0" x2="1" y2="1">
        <stop offset="0" stop-color="var(--photo-a)"/>
        <stop offset="1" stop-color="var(--photo-b)"/>
      </linearGradient>
    </defs>
    <path d="M470 40 C560 20 700 18 789 30 L789 300 C720 330 600 335 520 320 C470 300 440 220 450 150 C455 100 455 60 470 40 Z" fill="var(--yellow)"/>
  </svg>
  <div class="top-band abs"></div>
  <svg class="abs" width="789" height="540" viewBox="0 0 789 540" style="left:0;top:0">
    <path role="img" aria-label="Photo of a smiling young woman holding an ad sign" d="M482 52 C570 34 700 32 789 42 L789 288 C720 318 605 322 528 308 C484 290 460 215 468 150 C472 105 470 70 482 52 Z" fill="url(#photoTone)"/>
  </svg>
  <div class="brand front-brand abs">
    <span class="brand__dot"></span>
    <div>
      <div class="brand__name">Our Village Savers</div>
      <div class="brand__tag">Supporting local Businesses of America</div>
    </div>
  </div>
  <div class="ad-sign abs"><span>GET YOUR</span><span>AD HERE</span></div>

  <h1 class="headline abs">
    <span class="h-blue">Expose</span>
    <span class="h-ink">Your Business</span>
    <span class="h-blue">to THOUSANDS</span>
    <span class="h-small">of local shoppers</span>
  </h1>

  <div class="call abs">
    <div class="call__label">CALL US ON:</div>
    <div class="call__number">1-860-555-0182</div>
  </div>
  <div class="divider abs"></div>
  <ul class="features abs">
    <li>Local Independent Businesses</li>
    <li>Free Community Discount Card Program</li>
    <li>News &amp; Events</li>
    <li>Marketplace &amp; more</li>
  </ul>

  <svg class="abs bottom-band" width="789" height="90" viewBox="0 0 789 90" aria-hidden="true">
    <path d="M0 22 C200 0 560 0 789 20 L789 90 L0 90 Z" fill="var(--yellow)"/>
    <path d="M0 32 C220 12 560 12 789 30 L789 90 L0 90 Z" fill="var(--blue)"/>
  </svg>
  <div class="url abs">www.ourvillagesavers.example</div>
</section>

<section class="card card--back" aria-label="Postcard back">
  <svg class="abs back-panel" width="789" height="540" viewBox="0 0 789 540" aria-hidden="true">
    <path d="M0 150 L360 150 C430 150 470 230 450 320 C430 410 440 480 470 540 L0 540 Z" fill="var(--yellow)"/>
    <path d="M0 158 L350 158 C418 158 455 232 436 320 C418 406 424 476 452 540 L0 540 Z" fill="var(--blue)"/>
  </svg>
  <p class="intro abs">Welcome to the town's newest online city guide, built for your own community. Our Village Savers features local news, business listings, weather, events, reviews and more. As a member you can post a classified ad for almost anything you want to sell or share with neighbors. Whether you live here or are just passing through, we help you find what you need.</p>

  <div class="benefits abs">
    <h2 class="benefits__title">Benefits of Advertising:</h2>
    <ul class="benefits__list">
      <li>365 Days of Advertising</li>
      <li>Under $.04 per home</li>
      <li>Unlimited Social Media Attention</li>
      <li>Increased Revenue</li>
      <li>100% Managed for you</li>
    </ul>
  </div>
  <p class="fact abs">87% of online users depend on the internet to access local discounts. Business who use the internet to promote and sell their offline goods and services have grown 46% faster over the past two years.</p>

  <div class="brand back-brand abs">
    <span class="brand__dot"></span>
    <div>
      <div class="brand__name">Our Village Savers</div>
      <div class="brand__tag">Supporting local Businesses of America</div>
    </div>
  </div>
  <address class="return abs" style="font-style:normal">P.O Box 748, Putnam, CT 06917<br>www.ourvillagesavers.example</address>

  <div class="stamp abs" aria-label="Stamp area"></div>
  <div class="price abs"><span class="price__value">$.04</span><span class="price__unit">per home</span></div>
  <div class="growth abs"><span class="growth__value">46%</span><span class="growth__unit">faster</span></div>
  <div class="mail-lines abs" aria-hidden="true"><span></span><span></span><span></span><span></span></div>
</section>

</body>
</html>
```